Business Card Design Project - Zorvex Labs

High quality business card Must be funky.

We are an IT support from home and office, but our image is more retro.

Our logo is black and lime green. IT should be a 2 sided card with the multiple coloured ties somehow used on the reverse side (be creative!)

Black or white background fine or a combo of both

Target Market(s)

consumer and business

Industry/Entity Type

Business

```html
<!DOCTYPE html>
<html lang="en">
<head>
<meta charset="utf-8">
<title>Zorvex Labs — Business Card</title>
<link rel="stylesheet" href="https://fonts.googleapis.com/css2?family=Cabin:wght@400;500;600&display=swap">
<style>
  :root {
    --stage: #2a2a2a;
    --card-dark: #1b1a1c;
    --card-light: #ffffff;
    --card-light-shade: #e9e9e9;
    --lime: #8cc63f;
    --white: #f4f4f4;
    --grey: #c9c9c9;
    --tie-lime: #9bd12a;
    --tie-pink: #ec3f7c;
    --tie-cyan: #2bb8d6;
    --tie-red: #e8283c;
    --tie-dark: #2b2b2b;
  }
  * { box-sizing: border-box; margin: 0; padding: 0; }
  html, body {
    width: 1200px; height: 901px; overflow: hidden;
    background: var(--stage);
    font-family: "Cabin", "Gill Sans", sans-serif;
  }
  .stage {
    width: 1200px; height: 901px;
    display: flex; flex-direction: column;
    align-items: center; justify-content: center; gap: 44px;
  }
  .card {
    position: relative;
    width: 680px; height: 388px;
    border-radius: 26px;
    overflow: hidden;
  }
  /* Front */
  .card-front { background: var(--card-dark); color: var(--white); }
  .brand {
    position: absolute; left: 58px; top: 64px;
    display: flex; align-items: center; gap: 14px;
  }
  .brand-mark {
    width: 18px; height: 18px; border-radius: 50%;
    background: var(--lime);
  }
  .brand-name {
    font-size: 58px; font-weight: 600; color: var(--white);
    letter-spacing: -0.5px; line-height: 1;
  }
  .person { position: absolute; left: 62px; top: 208px; }
  .person-name {
    font-size: 23px; font-weight: 500; color: var(--lime);
    letter-spacing: 0.6px; text-transform: uppercase;
  }
  .person-title { font-size: 17px; color: var(--grey); margin-top: 2px; }
  .contacts {
    position: absolute; left: 62px; top: 278px;
    display: grid; grid-template-columns: 74px auto; row-gap: 4px;
    font-size: 19px; line-height: 1.2;
  }
  .contact-label { color: var(--lime); }
  .contact-value { color: var(--white); }
  .website {
    position: absolute; right: 56px; top: 214px;
    font-size: 19px; color: var(--lime);
  }
  /* Back */
  .card-back {
    background: radial-gradient(ellipse at 60% 30%, var(--card-light) 0%, var(--card-light) 45%, var(--card-light-shade) 100%);
  }
  .tie-row {
    position: absolute; left: 70px; right: 70px; top: 140px; height: 108px;
    border-radius: 12px;
    background: linear-gradient(90deg,
      var(--tie-lime) 0%, var(--tie-pink) 22%, var(--tie-cyan) 42%,
      var(--tie-red) 62%, var(--tie-dark) 80%, var(--tie-lime) 100%);
    opacity: 0.85;
  }
</style>
</head>
<body>
  <main class="stage">
    <section class="card card-front" aria-label="Business card front">
      <div class="brand">
        <span class="brand-mark"></span>
        <span class="brand-name">Zorvex Labs</span>
      </div>
      <div class="person">
        <p class="person-name">Marcus Delaney</p>
        <p class="person-title">Managing Director</p>
      </div>
      <div class="contacts">
        <span class="contact-label">Hotline</span><span class="contact-value">5550 123 456</span>
        <span class="contact-label">Mobile</span><span class="contact-value">8880 246 810</span>
        <span class="contact-label">Email</span><span class="contact-value">info@zorvexlabs.asia</span>
      </div>
      <p class="website">www.zorvexlabs.asia</p>
    </section>

    <section class="card card-back" aria-label="Business card back">
      <div class="tie-row" role="img" aria-label="Row of six neckties in lime, pink, cyan, red, striped and dotted green"></div>
    </section>
  </main>
</body>
</html>
```